Marvantar - Seafood industry professional promoting page

Hi. I´m in the seafood business with a one man company sourcing and exporting frozen seafood. I need to make a one page homepage for Marvantar (from Iceland). The feeling of it should be; Trustworthy, experience and knowledge.
Using as background a picture (or part of it), or a moving video:

http://www1.brelvik.is/sjorinn/myndir/ufsinn.jpg
https://clipvera.com/583720415

Main text to be:

- We can help source, market and add value to your seafood business
- Years of experience in seafood trade and production
- Extensive knowledge of fishing, seasonality, production and accreditations

Contact:
dagur@marvantar.is
Tel: +3654170392
(with a photo)

p.s. please also make logo look better.

Target Market(s)

Seafood industry

Industry/Entity Type

Business

Logo Text

Marvantar

Coding

Coded - Design and coding required

Number of Pages Required

1 page

Colors
0792cd
33a6d7

```html
<!DOCTYPE html>
<html lang="en">
<head>
<meta charset="utf-8">
<title>Marvantar – Seafood sourcing and export</title>
<link rel="stylesheet" href="https://fonts.googleapis.com/css2?family=Open+Sans:wght@300;400;600;700&display=swap">
<style>
  :root {
    --brand: #0792cd;
    --brand-light: #33a6d7;
    --button: #3d7be0;
    --navy: #0f1a45;
    --deep-blue: #12327a;
    --ink: #1d2a4d;
    --white: #ffffff;
    --paper: #ededed;
    --field: #f2f2f2;
    --field-line: #dcdcdc;
    --muted: #8a8f99;
  }
  * { box-sizing: border-box; margin: 0; padding: 0; }
  html, body { width: 1200px; height: 2272px; overflow: hidden; }
  body {
    font-family: "Open Sans", Arial, sans-serif;
    color: var(--ink);
    background: var(--white);
    position: relative;
  }

  /* Header */
  .site-header {
    position: absolute; top: 0; left: 0; width: 1200px; height: 68px;
    background: var(--white);
    display: flex; align-items: center; justify-content: space-between;
    padding: 0 56px 0 40px;
  }
  .brand { display: flex; align-items: center; gap: 10px; }
  .brand-dot { width: 26px; height: 26px; border-radius: 50%; background: var(--brand); }
  .brand-name { font-weight: 700; font-size: 22px; color: var(--deep-blue); letter-spacing: 0.5px; }
  .header-cta {
    background: var(--button); color: var(--white);
    font-size: 13px; font-weight: 600;
    padding: 6px 18px; border-radius: 14px;
  }

  /* Hero panels */
  .panel {
    position: absolute; left: 0; width: 1200px; overflow: hidden;
  }
  .panel-bg { position: absolute; inset: 0; }
  .panel-one { top: 68px; height: 540px; }
  .panel-one .panel-bg {
    background: radial-gradient(ellipse at 30% 30%, #1f4c9c 0%, #143a86 45%, #0c2a6a 100%);
  }
  .panel-two { top: 608px; height: 572px; }
  .panel-two .panel-bg {
    background: linear-gradient(180deg, #a94f8f 0%, #7b4c95 45%, #3e4ea3 100%);
  }
  .panel-three { top: 1180px; height: 568px; }
  .panel-three .panel-bg {
    background: linear-gradient(180deg, #b9508b 0%, #8a4f96 40%, #3e4aa0 80%, #25408f 100%);
  }
  .panel-text {
    position: absolute; left: 312px; width: 620px;
    color: var(--white); font-weight: 300;
    font-size: 40px; line-height: 48px;
  }
  .panel-one .panel-text { top: 152px; }
  .panel-two .panel-text { top: 232px; }
  .panel-three .panel-text { top: 156px; }

  .scroll-btn {
    position: absolute; width: 30px; height: 30px;
  }
  .scroll-down { left: 585px; }
  .scroll-up { left: 1110px; }

  /* Contact */
  .contact {
    position: absolute; top: 1748px; left: 0; width: 1200px; height: 444px;
    background: var(--paper);
  }
  .contact-photo {
    position: absolute; left: 248px; top: 52px; width: 180px; height: 308px;
    background: linear-gradient(180deg, #cfd8de 0%, #9aa7b0 35%, #4f5f6a 70%, #2f3e48 100%);
  }
  .contact-info { position: absolute; left: 442px; top: 52px; }
  .contact-title { font-size: 16px; font-weight: 400; color: var(--button); margin-bottom: 12px; }
  .contact-row {
    display: flex; align-items: center; gap: 12px;
    font-size: 14px; color: var(--button); margin-bottom: 12px;
  }
  .contact-row svg { width: 20px; height: 20px; }

  .contact-form {
    position: absolute; left: 724px; top: 52px; width: 216px; height: 308px;
    background: var(--white); padding: 20px 18px;
  }
  .form-title { font-size: 14px; color: var(--ink); margin-bottom: 12px; }
  .form-field {
    width: 100%; height: 36px; background: var(--field);
    border: 1px solid var(--field-line); border-radius: 3px;
    font-size: 11px; color: var(--muted); padding: 10px 10px; margin-bottom: 12px;
  }
  .form-field.message { height: 80px; }
  .form-submit {
    display: block; margin: 8px auto 0; width: 130px; height: 28px;
    background: var(--button); color: var(--white); border-radius: 14px;
    font-size: 11px; font-weight: 600; text-align: center; line-height: 28px;
  }

  /* Footer */
  .site-footer {
    position: absolute; top: 2192px; left: 0; width: 1200px; height: 80px;
    background: var(--navy);
  }
  .copyright {
    position: absolute; left: 540px; top: 34px; font-size: 10px; color: #9aa3c0;
  }
  .social-dot {
    position: absolute; left: 852px; top: 34px; width: 12px; height: 12px;
    border-radius: 50%; background: #c6cce0;
  }
  .footer-up { position: absolute; left: 1110px; top: 25px; width: 30px; height: 30px; }
</style>
</head>
<body>

<header class="site-header">
  <div class="brand">
    <span class="brand-dot"></span>
    <span class="brand-name">Marvantar</span>
  </div>
  <span class="header-cta">Contact Us</span>
</header>

<section class="panel panel-one">
  <div class="panel-bg" role="img" aria-label="Close-up photo of fresh fish on ice, tinted deep blue"></div>
  <h1 class="panel-text">We can help source, market and add value to your seafood business</h1>
  <svg class="scroll-btn scroll-down" style="top:480px" viewBox="0 0 30 30"><circle cx="15" cy="15" r="13" fill="rgba(255,255,255,0.18)"/><path d="M15 9v11M10 15l5 5 5-5" stroke="#fff" stroke-width="1.6" fill="none"/></svg>
</section>

<section class="panel panel-two">
  <div class="panel-bg" role="img" aria-label="Photo of a catch of whole fish, tinted pink to blue"></div>
  <h2 class="panel-text">Experienced in seafood trade and production</h2>
  <svg class="scroll-btn scroll-down" style="top:505px" viewBox="0 0 30 30"><circle cx="15" cy="15" r="13" fill="rgba(255,255,255,0.18)"/><path d="M15 9v11M10 15l5 5 5-5" stroke="#fff" stroke-width="1.6" fill="none"/></svg>
  <svg class="scroll-btn scroll-up" style="top:517px" viewBox="0 0 30 30"><circle cx="15" cy="15" r="13" fill="rgba(255,255,255,0.22)"/><path d="M15 21V10M10 15l5-5 5 5" stroke="#fff" stroke-width="1.6" fill="none"/></svg>
</section>

<section class="panel panel-three">
  <div class="panel-bg" role="img" aria-label="Photo of a fishing vessel at sea, tinted pink to blue"></div>
  <h2 class="panel-text">Extensive knowledge of fishing, seasonality, production and accreditations</h2>
  <svg class="scroll-btn scroll-down" style="top:505px" viewBox="0 0 30 30"><circle cx="15" cy="15" r="13" fill="rgba(255,255,255,0.18)"/><path d="M15 9v11M10 15l5 5 5-5" stroke="#fff" stroke-width="1.6" fill="none"/></svg>
  <svg class="scroll-btn scroll-up" style="top:513px" viewBox="0 0 30 30"><circle cx="15" cy="15" r="13" fill="rgba(255,255,255,0.22)"/><path d="M15 21V10M10 15l5-5 5 5" stroke="#fff" stroke-width="1.6" fill="none"/></svg>
</section>

<section class="contact">
  <div class="contact-photo" role="img" aria-label="Photo of a man standing waist-deep in water, seen from behind"></div>
  <div class="contact-info">
    <h3 class="contact-title">Contact us</h3>
    <div class="contact-row">
      <svg viewBox="0 0 20 20"><rect x="2" y="4.5" width="16" height="11" rx="1.5" fill="none" stroke="#3d7be0" stroke-width="1.4"/><path d="M2.5 5.5l7.5 6 7.5-6" fill="none" stroke="#3d7be0" stroke-width="1.4"/></svg>
      <span>dagur@marvantar.is</span>
    </div>
    <div class="contact-row">
      <svg viewBox="0 0 20 20"><rect x="6" y="2" width="8" height="16" rx="1.5" fill="none" stroke="#3d7be0" stroke-width="1.4"/><circle cx="10" cy="15" r="0.9" fill="#3d7be0"/></svg>
      <span>+3654170392</span>
    </div>
  </div>
  <form class="contact-form">
    <p class="form-title">Ready to get started?</p>
    <div class="form-field">Your Name</div>
    <div class="form-field">Email</div>
    <div class="form-field message">Message</div>
    <span class="form-submit">Send Message</span>
  </form>
</section>

<footer class="site-footer">
  <p class="copyright">© Copyright 2016 Marvantar. All rights reserved.</p>
  <span class="social-dot"></span>
  <svg class="footer-up" viewBox="0 0 30 30"><circle cx="15" cy="15" r="13" fill="rgba(255,255,255,0.15)"/><path d="M15 21V10M10 15l5-5 5 5" stroke="#fff" stroke-width="1.6" fill="none"/></svg>
</footer>

</body>
</html>
```